Young Architect Bussiness Card

English is not my first language (spanish is).
Need a bussiness card design for my best friend who is about to graduate from college, Licentiate degree in architecture, so she needs business cards to start networking, currently she has no porfolio, web page or facebook. so she is relying on her cel phone and gmail, but should leave space for one of them (facebook)

Design for business card should be modern, maybe something with construction blue prints patern or 3D modelling.

Name: Mariela Fonseca Arrieta
Licentiate in Arquitecture
Cel: (506) XXX-4827
email: marielaXXX@correovela.com

Services, although im not sure if it has to be there or not:
Anteproyectos / Proposal design
Inspecciones / Site Inspections
Modelado 3D / 3D modelling
Planos Constructivos / Construction Blue Prints
Presupuestos / Budgets

Design should be in spanish

Contact Information for Business Card

Name: Mariela Fonseca, Arquitecto
Associtation code : XXXX
Phone: (506) XXXX-XXXX
Email: xxx@correovela.com
Facebook: xxxx

Requirements
Must have
• Design for business card should be modern, maybe something with construction blue prints patern or 3D modelling.
Nice to have
• Something like a transition from 2D to 3D.

```html
<!DOCTYPE html>
<html lang="es">
<head>
<meta charset="utf-8">
<title>Tarjeta de presentación – Mariela Fonseca Arrieta</title>
<link rel="stylesheet" href="https://fonts.googleapis.com/css2?family=Open+Sans:wght@400;600;700&display=swap">
<style>
  :root {
    --bg: #2b2c2e;
    --blue-dark: #3d63b2;
    --blue-light: #5a85cc;
    --blue-ink: #3b62b6;
    --photo-a: #8496d2;
    --photo-b: #5e71b6;
    --paper: #f5f6f9;
    --ink: #2a2c33;
    --white: #ffffff;
  }
  * { margin: 0; padding: 0; box-sizing: border-box; }
  html, body {
    width: 1200px; height: 900px; overflow: hidden;
    background: var(--bg);
    font-family: "Open Sans", Arial, sans-serif;
  }
  .stage { position: relative; width: 1200px; height: 900px; }
  .card {
    position: absolute; left: 250px; width: 700px; height: 400px;
    overflow: hidden; box-shadow: 0 10px 30px rgba(0,0,0,.45);
  }
  .card--front { top: 40px; background: linear-gradient(160deg, var(--blue-dark), var(--blue-light)); }
  .card--back { top: 470px; background: var(--paper); }
  .card__art { position: absolute; left: 0; top: 0; }

  .front__name {
    position: absolute; left: 0; right: 0; top: 150px; text-align: center;
    color: var(--white); font-weight: 600; font-size: 36px; letter-spacing: .3px;
  }
  .front__title {
    position: absolute; left: 0; right: 0; top: 200px; text-align: center;
    color: rgba(255,255,255,.85); font-size: 18px;
  }
  .front__services {
    position: absolute; left: 145px; right: 60px; top: 342px;
    color: var(--white); font-size: 12.5px; text-align: center; white-space: nowrap;
  }
  .front__services span + span::before { content: " • "; }

  .back__name {
    position: absolute; left: 92px; top: 92px; white-space: nowrap;
    color: var(--blue-ink); font-weight: 700; font-size: 26px;
  }
  .back__title {
    position: absolute; left: 92px; top: 130px;
    color: var(--ink); font-size: 18px;
  }
  .contacts { position: absolute; left: 90px; top: 246px; list-style: none; }
  .contacts li {
    display: flex; align-items: center; gap: 12px;
    color: var(--ink); font-size: 17px; height: 28px; white-space: nowrap;
  }
  .contacts .icon { width: 20px; height: 20px; flex: none; display: block; }
  .contacts .icon--square { width: 18px; height: 18px; background: var(--blue-ink); border-radius: 3px; margin: 0 1px; }
</style>
</head>
<body>
<main class="stage">

  <section class="card card--front">
    <svg class="card__art" width="700" height="400" viewBox="0 0 700 400">
      <g fill="none" stroke="#ffffff" stroke-width="2">
        <polyline points="120,350 40,350 40,40 660,40 660,350 640,350"/>
      </g>
    </svg>
    <h1 class="front__name">Mariela Fonseca Arrieta</h1>
    <p class="front__title">Licentiate in Arquitecture</p>
    <p class="front__services">
      <span>Anteproyectos</span><span>Inspecciones</span><span>Modelado 3D</span><span>Planos Constructivos</span><span>Presupuestos</span>
    </p>
  </section>

  <section class="card card--back">
    <svg class="card__art" width="700" height="400" viewBox="0 0 700 400">
      <defs>
        <linearGradient id="photoTone" x1="0" y1="0" x2="1" y2="1">
          <stop offset="0" stop-color="#8496d2"/>
          <stop offset="1" stop-color="#5e71b6"/>
        </linearGradient>
      </defs>
      <polygon class="back__photo" points="430,0 700,0 700,400 485,400" fill="url(#photoTone)"
        role="img" aria-label="Fotografía de estructura arquitectónica con planos constructivos, en tono azul"/>
      <g fill="none" stroke="#3b62b6" stroke-width="2.5">
        <polyline points="70,240 70,70 424,70"/>
        <polyline points="112,352 112,370 470,370"/>
      </g>
    </svg>
    <h2 class="back__name">Mariela Fonseca Arrieta</h2>
    <p class="back__title">Licentiate in Arquitecture</p>
    <ul class="contacts">
      <li>
        <svg class="icon" viewBox="0 0 20 20"><path fill="#3b62b6" d="M2 7c0-2 3-4 8-4s8 2 8 4v2h-4V7c0-.6-2-1-4-1s-4 .4-4 1v2H2z M4 10h12l1 7H3z"/></svg>
        <span>(506) XXX-4827</span>
      </li>
      <li>
        <svg class="icon" viewBox="0 0 20 20"><rect x="1" y="4" width="18" height="12" fill="#3b62b6"/><polyline points="1,4 10,11 19,4" fill="none" stroke="#fff" stroke-width="1.5"/></svg>
        <span>youremail@correovela.com</span>
      </li>
      <li><span class="icon icon--square"></span><span>redvela.com/yourpage</span></li>
      <li><span class="icon icon--square"></span><span>trinovela.com/yourpage</span></li>
    </ul>
  </section>

</main>
</body>
</html>
```